Bluefern painting and decorating *

Need a flyer design to advertise my services
So the information I need included is the services we offer at bluefern painting and decorating which include
Interior painting
Exterior painting
Wallpaper hanging
Paint and cellulose spraying
Dust free sanding
Pressure washing
Stone cleaning
Also would need to have my company contact details in
Www.bluefernpaintingdecorating.co.uk
Email is info@bluefernpaintingdecorating.com
Bluefern Painting & Decorating Services has a proven track record of innovative designs, effective problem solving and attention to detail and our goal is to meet and exceed the expectations of every customer. We take on all types of jobs from small domestic work to larger commercial projects, all carried out to the highest standards, and at very competitive prices.

```html
<!DOCTYPE html>
<html lang="en">
<head>
<meta charset="utf-8">
<title>Bluefern Painting and Decorating – Flyer</title>
<link rel="stylesheet" href="https://fonts.googleapis.com/css2?family=Open+Sans:wght@400;600;700;800&display=swap">
<style>
  :root {
    --bg: #e4e4e4;
    --paper: #ffffff;
    --blue: #2b7cc6;
    --blue-light: #3a8ad0;
    --navy: #173f6e;
    --ink: #1f4f86;
    --footer: #3a3b3d;
    --footer-text: #d9dbde;
    --white: #ffffff;
  }
  * { box-sizing: border-box; margin: 0; padding: 0; }
  html, body { width: 1200px; height: 960px; overflow: hidden; }
  body { background: var(--bg); font-family: "Open Sans", sans-serif; }

  .flyer {
    position: absolute; left: 280px; top: 27px;
    width: 640px; height: 906px;
    background: var(--paper);
    overflow: hidden;
    box-shadow: 0 10px 30px rgba(0,0,0,.18);
  }
  .flyer-art { position: absolute; inset: 0; width: 640px; height: 906px; }

  .logo {
    position: absolute; left: 240px; top: 240px; width: 160px;
    text-align: center; color: var(--ink);
  }
  .logo-name { font-size: 27px; font-weight: 700; letter-spacing: .5px; line-height: 1; }
  .logo-tagline { font-size: 6.6px; font-weight: 600; letter-spacing: .2px; margin-top: 3px; }
  .logo-rule { width: 120px; height: 1px; background: var(--ink); margin: 6px auto 0; }

  .why {
    position: absolute; left: 405px; top: 228px; width: 235px;
    text-align: center; color: var(--white);
  }
  .why-title { font-size: 22px; font-weight: 700; }
  .why-rule { width: 170px; height: 1px; background: var(--white); margin: 6px auto 18px; }
  .why-list { list-style: none; font-size: 16px; font-weight: 700; line-height: 33px; }

  .intro {
    position: absolute; left: 160px; top: 455px; width: 320px;
    text-align: center; color: var(--white);
    text-shadow: 0 1px 3px rgba(0,0,0,.45);
  }
  .intro-title { font-size: 23px; font-weight: 700; line-height: 1.1; }
  .intro-sub { font-size: 23px; font-weight: 400; line-height: 1.2; }
  .intro-text { font-size: 11.5px; line-height: 1.35; margin-top: 12px; padding: 0 14px; }

  .services { position: absolute; list-style: none; color: var(--ink); }
  .services li { display: flex; align-items: center; gap: 7px; white-space: nowrap; }
  .services li::before {
    content: ""; width: 6px; height: 6px; border: 1px solid var(--ink);
    transform: rotate(45deg); flex: none;
  }
  .services-left { left: 20px; top: 620px; font-size: 11px; line-height: 21px; }
  .services-right { right: 18px; top: 606px; font-size: 13.5px; line-height: 23.5px; text-align: right; }
  .services-right li { flex-direction: row-reverse; }

  .features { position: absolute; left: 0; top: 772px; width: 640px; height: 80px; display: flex; }
  .feature {
    display: flex; flex-direction: column; align-items: center; justify-content: center;
    gap: 6px; color: var(--white); font-size: 10.5px; font-weight: 700;
  }
  .feature-experience { width: 185px; background: var(--blue); }
  .feature-quality { width: 235px; background: var(--navy); }
  .feature-prices { width: 220px; background: var(--blue); }
  .feature svg { width: 26px; height: 26px; }

  .footer {
    position: absolute; left: 0; top: 852px; width: 640px; height: 54px;
    background: var(--footer); color: var(--footer-text);
    display: flex; align-items: center; padding: 0 20px; font-size: 11.5px;
  }
  .contacts { display: flex; flex-direction: column; gap: 3px; }
  .contacts-row { display: flex; gap: 24px; }
  .contact { display: flex; align-items: center; gap: 6px; }
  .contact svg { width: 12px; height: 12px; flex: none; }
  .social { margin-left: auto; display: flex; gap: 9px; }
  .social span { width: 18px; height: 18px; border-radius: 50%; background: var(--blue); }
  .social span:nth-child(1) { background: #2f5a9e; }
  .social span:nth-child(4) { background: #3aa34a; }
  .social span:nth-child(5) { background: #6d6f72; }
</style>
</head>
<body>
<main class="flyer">
  <svg class="flyer-art" viewBox="0 0 640 906">
    <defs>
      <linearGradient id="g-living" x1="0" y1="0" x2="1" y2="1">
        <stop offset="0" stop-color="#8c8f8c"/><stop offset=".45" stop-color="#1e9fb4"/><stop offset="1" stop-color="#e9e7e2"/>
      </linearGradient>
      <linearGradient id="g-lounge" x1="0" y1="0" x2="0" y2="1">
        <stop offset="0" stop-color="#d9d3c5"/><stop offset=".6" stop-color="#b9ad9b"/><stop offset="1" stop-color="#5b5650"/>
      </linearGradient>
      <linearGradient id="g-blue" x1="0" y1="0" x2="0" y2="1">
        <stop offset="0" stop-color="#2f7fc8"/><stop offset="1" stop-color="#2874bb"/>
      </linearGradient>
      <linearGradient id="g-kitchen" x1="0" y1="0" x2="0" y2="1">
        <stop offset="0" stop-color="#cfd3d6"/><stop offset=".5" stop-color="#8f8e8a"/><stop offset="1" stop-color="#b58a5e"/>
      </linearGradient>
      <linearGradient id="g-yellow" x1="0" y1="0" x2="0" y2="1">
        <stop offset="0" stop-color="#e9cf52"/><stop offset="1" stop-color="#c8a26a"/>
      </linearGradient>
      <linearGradient id="g-teal" x1="0" y1="0" x2="0" y2="1">
        <stop offset="0" stop-color="#2c4f63"/><stop offset="1" stop-color="#5a3b36"/>
      </linearGradient>
      <linearGradient id="g-office" x1="0" y1="0" x2="0" y2="1">
        <stop offset="0" stop-color="#bcd3e3"/><stop offset="1" stop-color="#8fb3cc"/>
      </linearGradient>
      <linearGradient id="g-lobby" x1="0" y1="0" x2="0" y2="1">
        <stop offset="0" stop-color="#d8d4ca"/><stop offset="1" stop-color="#9d8f7e"/>
      </linearGradient>
      <linearGradient id="g-lower" x1="0" y1="0" x2="0" y2="1">
        <stop offset="0" stop-color="#ffffff"/><stop offset="1" stop-color="#eef0f2"/>
      </linearGradient>
    </defs>

    <rect x="0" y="560" width="640" height="220" fill="url(#g-lower)"/>

    <polygon role="img" aria-label="Photo: living room with a teal feature wall, wooden sideboard and striped rug"
             points="0,0 640,0 640,62 320,226 0,72" fill="url(#g-living)"/>
    <polygon role="img" aria-label="Photo: bright lounge with cream sofa and cushions"
             points="0,88 240,212 240,420 0,420" fill="url(#g-lounge)"/>
    <polygon points="640,80 400,212 400,412 640,412" fill="url(#g-blue)"/>

    <polygon role="img" aria-label="Photo: open-plan kitchen and dining room with pendant lights"
             points="143,432 240,376 240,300 400,300 400,376 497,432 497,634 320,736 143,634" fill="url(#g-kitchen)"/>

    <rect role="img" aria-label="Photo: room with a yellow wall and sofa" x="16" y="420" width="127" height="94" fill="url(#g-yellow)"/>
    <rect role="img" aria-label="Photo: dark teal room with fireplace" x="16" y="514" width="127" height="92" fill="url(#g-teal)"/>
    <rect role="img" aria-label="Photo: modern office with glass partitions" x="497" y="420" width="143" height="90" fill="url(#g-office)"/>
    <rect role="img" aria-label="Photo: office lounge with armchairs" x="497" y="510" width="143" height="88" fill="url(#g-lobby)"/>

    <polygon points="320,172 400,218 400,318 320,364 240,318 240,218" fill="#ffffff"/>
  </svg>

  <div class="logo">
    <div class="logo-name">BLUEFERN</div>
    <div class="logo-tagline">PAINTING AND DECORATING SERVICES</div>
    <div class="logo-rule"></div>
  </div>

  <section class="why">
    <h2 class="why-title">Why choose us?</h2>
    <div class="why-rule"></div>
    <ul class="why-list">
      <li>Professional Services</li>
      <li>Team of Experts</li>
      <li>Free quotes</li>
    </ul>
  </section>

  <section class="intro">
    <h1 class="intro-title">Established decorators</h1>
    <p class="intro-sub">in South London</p>
    <p class="intro-text">Get in touch with our expert decorators at Bluefern Painting and Decorating Services in Bexley to give your property a makeover. Our services are available across South London.</p>
  </section>

  <ul class="services services-left">
    <li>Interior painting</li>
    <li>Exterior painting</li>
    <li>Wallpaper hanging</li>
    <li>Paint and cellulose spraying</li>
    <li>Dust free sanding</li>
    <li>Pressure washing</li>
    <li>Stone cleaning</li>
  </ul>

  <ul class="services services-right">
    <li>Paint stripping</li>
    <li>Artex removal</li>
    <li>Protective coatings</li>
    <li>Wall and floor tiling</li>
    <li>Wall and floor painting</li>
    <li>Decorative paint effects</li>
    <li>Internal and external decorating</li>
  </ul>

  <section class="features">
    <div class="feature feature-experience">
      <svg viewBox="0 0 26 26" fill="none" stroke="#fff" stroke-width="1.3"><circle cx="13" cy="10" r="7"/><path d="M9 16l-2 8 6-3 6 3-2-8"/></svg>
      <span>Over 12 years of experience</span>
    </div>
    <div class="feature feature-quality">
      <svg viewBox="0 0 26 26" fill="none" stroke="#fff" stroke-width="1.5"><circle cx="13" cy="13" r="11"/><path d="M8 13.5l3.5 3.5 7-7.5"/></svg>
      <span>Quality craftsmanship</span>
    </div>
    <div class="feature feature-prices">
      <svg viewBox="0 0 26 26" fill="none" stroke="#fff" stroke-width="1.3"><circle cx="13" cy="13" r="11"/><text x="13" y="18" text-anchor="middle" font-size="14" fill="#fff" stroke="none" font-family="Open Sans, sans-serif">£</text></svg>
      <span>Competitive prices</span>
    </div>
  </section>

  <footer class="footer">
    <div class="contacts">
      <div class="contacts-row">
        <div class="contact">
          <svg viewBox="0 0 12 12"><path d="M2.5 1l2 2.5-1 1.3c.6 1.3 1.6 2.3 2.8 2.9l1.3-1 2.4 2-1.2 1.8C5 10.5 1.3 6.8.7 2.3z" fill="#3a8ad0"/></svg>
          <span>07700 900 123</span>
        </div>
        <div class="contact">
          <svg viewBox="0 0 12 12"><rect x="1" y="2.5" width="10" height="7" fill="#3a8ad0"/><path d="M1 2.5l5 4 5-4" stroke="#3a3b3d" fill="none"/></svg>
          <span>info@bluefernpaintingdecorating.com</span>
        </div>
      </div>
      <div class="contact">
        <svg viewBox="0 0 12 12" fill="none" stroke="#3a8ad0" stroke-width="1.1"><circle cx="6" cy="6" r="5"/><path d="M1 6h10M6 1c-2.5 3-2.5 7 0 10M6 1c2.5 3 2.5 7 0 10"/></svg>
        <span>www.bluefernpaintingdecorating.co.uk</span>
      </div>
    </div>
    <div class="social" aria-label="Social media links">
      <span></span><span></span><span></span><span></span><span></span>
    </div>
  </footer>
</main>
</body>
</html>
```